Re-style home page - eye-catching and unique design for social commerce website

We need a new concept design for TrindaMo's home page.
We don't want to make huge changes but creating a more professional and eye-catching style.

We need to look very serious like a professional services company and in the same time to look like a social network for e-commerce.

Our logo is very captive and you can use to creating something of harmonious.

This is a re-style and I'm excepted to see unique and fresh design like Clovaret.

Target Market(s)

e-commerce and social

Industry/Entity Type

Social

Number of Pages Required

1 page

Font styles to use
Serif
Sans Serif

Requirements
Must have
• An eye-catching result.
• Search bar with logo and Login How it works and business
• The slogan with login and signup.
• Footer links.
Nice to have
• I would like to open the home page and see only two clear ways:
• -Consumer
• --Search
• --The slogan
• --Login and Signup
• --How it works
• -Business
• --Go to Business area
• Background: City, Shopping.
Should not have
• Scrollbar style!

```html
<!DOCTYPE html>
<html lang="en">
<head>
<meta charset="utf-8">
<title>TrindaMo – Shop Directly From You Profile</title>
<link rel="stylesheet" href="https://fonts.googleapis.com/css2?family=Lato:wght@400;700&family=Open+Sans:wght@400;600;700&display=swap">
<style>
  :root {
    --night: #16110f;
    --night-mid: #3a2a24;
    --night-warm: #5a3b2a;
    --white: #ffffff;
    --orange: #ff6a3a;
    --orange-deep: #ff5230;
    --blue: #4b93cf;
    --blue-deep: #3d7fbe;
    --social-blue: #4a6cb8;
    --social-blue-dark: #3b5799;
    --green: #5fbf2a;
    --green-deep: #46a11c;
    --gold: #ab8a1c;
    --ink: #444444;
    --muted: #8a8a8a;
  }
  * { box-sizing: border-box; margin: 0; padding: 0; }
  html, body { width: 1200px; height: 624px; overflow: hidden; }
  body {
    position: relative;
    font-family: "Lato", Arial, sans-serif;
    color: var(--white);
    background: var(--night);
  }
  .city-backdrop {
    position: absolute; inset: 0;
    background:
      radial-gradient(ellipse at 12% 60%, rgba(200,120,60,.45), transparent 45%),
      radial-gradient(ellipse at 90% 55%, rgba(210,90,60,.4), transparent 45%),
      radial-gradient(ellipse at 50% 95%, rgba(190,130,70,.4), transparent 50%),
      linear-gradient(180deg, #0c0908 0%, var(--night-mid) 40%, var(--night-warm) 100%);
  }
  .color-stripe {
    position: absolute; left: 0; width: 1200px; height: 3px;
    background: linear-gradient(90deg,
      #f2c64a 0 8%, #6a6bd8 8% 16%, #e05c8a 16% 24%, #58b2e0 24% 32%,
      #9bc94a 32% 40%, #f29a3a 40% 48%, #6a6bd8 48% 56%, #e04a4a 56% 64%,
      #f2c64a 64% 72%, #58b2e0 72% 80%, #e05c8a 80% 88%, #9bc94a 88% 100%);
  }
  .color-stripe.top { top: 0; }
  .color-stripe.bottom { bottom: 0; }

  .site-header { position: absolute; top: 0; left: 0; width: 1200px; height: 70px; }
  .brand {
    position: absolute; left: 115px; top: 16px;
    font-family: "Open Sans", Arial, sans-serif; font-weight: 700;
    font-size: 34px; letter-spacing: -0.5px; color: var(--white);
  }
  .main-nav {
    position: absolute; left: 659px; top: 29px;
    font-size: 14px; display: flex; gap: 8px;
  }
  .main-nav .sep { opacity: .9; }
  .search-box {
    position: absolute; left: 891px; top: 23px; width: 193px; height: 33px;
    background: var(--white); border-radius: 2px;
    display: flex; align-items: center; justify-content: space-between;
    padding: 0 10px 0 15px; color: var(--ink); font-size: 11px;
  }

  .headline {
    position: absolute; top: 89px; left: 0; width: 1200px; text-align: center;
    font-family: "Open Sans", Arial, sans-serif; font-weight: 700; font-size: 30px;
  }

  .notebook { position: absolute; left: 190px; top: 147px; width: 806px; height: 409px; }
  .page-consumer {
    position: absolute; left: 0; top: 0; width: 359px; height: 409px;
    background: linear-gradient(160deg, var(--orange), var(--orange-deep));
    border-radius: 70px 0 0 70px / 90px 0 0 90px;
  }
  .page-business {
    position: absolute; left: 359px; top: 0; width: 447px; height: 409px;
    background: linear-gradient(160deg, var(--blue), var(--blue-deep));
    border-radius: 0 70px 70px 0 / 0 90px 90px 0;
  }
  .binding { position: absolute; left: 344px; top: 18px; }

  .page-title {
    position: absolute; font-family: "Open Sans", Arial, sans-serif;
    font-weight: 700; font-size: 33px; line-height: 1;
  }
  .page-consumer .page-title { left: 47px; top: 44px; }
  .tagline { position: absolute; left: 50px; top: 80px; font-size: 15px; }
  .rule { position: absolute; height: 1px; background: rgba(255,255,255,.25); box-shadow: 0 1px 2px rgba(0,0,0,.15); }
  .page-consumer .rule { left: 42px; top: 107px; width: 285px; }

  .social-login {
    position: absolute; left: 49px; top: 136px; width: 236px; height: 33px;
    display: flex; background: var(--social-blue); border-radius: 2px;
  }
  .social-login .mark { width: 42px; background: var(--social-blue-dark); display: flex; align-items: center; justify-content: center; }
  .social-login .mark span { width: 10px; height: 10px; background: var(--white); }
  .social-login .label {
    flex: 1; display: flex; align-items: center; justify-content: center;
    font-family: "Open Sans", Arial, sans-serif; font-weight: 700; font-size: 15px;
  }
  .field {
    position: absolute; left: 49px; width: 236px; height: 32px;
    background: linear-gradient(180deg, #ffffff, #ececec);
    border: 1px solid #e8e8e8; color: var(--muted); font-size: 10px;
    display: flex; align-items: center; padding-left: 12px;
  }
  .field.email { top: 177px; }
  .field.password { top: 218px; }
  .forgot-links {
    position: absolute; left: 48px; top: 259px; width: 238px;
    display: flex; justify-content: space-between; font-size: 10px;
  }
  .signup-btn {
    position: absolute; left: 47px; top: 289px; width: 105px; height: 36px;
    background: linear-gradient(180deg, var(--green), var(--green-deep));
    border: 2px solid #e84a20; border-radius: 3px;
    font-family: "Open Sans", Arial, sans-serif; font-weight: 700; font-size: 17px;
    display: flex; align-items: center; justify-content: center;
  }

  .page-business .page-title { left: 0; width: 440px; text-align: center; top: 44px; }
  .page-business .rule { left: 62px; top: 106px; width: 334px; }
  .feed-categories { position: absolute; left: 68px; top: 135px; }
  .tag-row { display: flex; gap: 4px; margin-bottom: 7px; }
  .tag {
    height: 28px; padding: 0 10px; font-size: 11.5px;
    border: 1px solid rgba(255,255,255,.35); color: #eef5fb;
    display: flex; align-items: center;
  }

  .site-footer {
    position: absolute; left: 0; top: 588px; width: 1200px; height: 33px;
    background: var(--gold);
  }
  .footer-links {
    position: absolute; left: 115px; top: 9px; font-size: 11px;
    display: flex; gap: 6px;
  }
  .social-links { position: absolute; left: 966px; top: 9px; display: flex; gap: 10px; align-items: center; }
  .social-links .dot { width: 13px; height: 13px; border-radius: 50%; background: var(--white); }
</style>
</head>
<body>
  <div class="city-backdrop" role="img" aria-label="Night city shopping street with glowing shop signs"></div>
  <div class="color-stripe top"></div>

  <header class="site-header">
    <div class="brand">TrindaMo</div>
    <nav class="main-nav">
      <span>How It Works</span><span class="sep">|</span><span>Business</span><span class="sep">|</span><span>Login</span>
    </nav>
    <div class="search-box">
      <span>Search</span>
      <svg width="13" height="13" viewBox="0 0 13 13"><circle cx="5" cy="5" r="3.6" fill="none" stroke="#555" stroke-width="1.6"/><line x1="7.6" y1="7.6" x2="12" y2="12" stroke="#555" stroke-width="2"/></svg>
    </div>
  </header>

  <h1 class="headline">Shop Directly From You Profile</h1>

  <main class="notebook">
    <section class="page-consumer">
      <h2 class="page-title">Save your Time</h2>
      <p class="tagline">Live better.</p>
      <div class="rule"></div>
      <div class="social-login"><div class="mark"><span></span></div><div class="label">Login with Friendloop</div></div>
      <div class="field email">Email</div>
      <div class="field password">Create a Password</div>
      <div class="forgot-links"><span>Forgot username</span><span>Forgot password</span></div>
      <div class="signup-btn">Sign Up</div>
    </section>

    <section class="page-business">
      <h2 class="page-title">Setup Your Feed</h2>
      <div class="rule"></div>
      <div class="feed-categories">
        <div class="tag-row"><span class="tag">Active Lite</span><span class="tag">Arts &amp; Entertainment</span><span class="tag">Automotive</span></div>
        <div class="tag-row"><span class="tag">Beauty &amp; Spas</span><span class="tag">Education</span><span class="tag">Event Planning &amp; Services</span></div>
        <div class="tag-row"><span class="tag">Food</span><span class="tag">Health &amp; Medical</span><span class="tag">Home Services</span><span class="tag">Hotels</span></div>
        <div class="tag-row"><span class="tag">Local Services</span><span class="tag">Mass Media</span><span class="tag">Nightluife</span><span class="tag">Pets</span></div>
        <div class="tag-row"><span class="tag">Professional Services</span><span class="tag">Public Services &amp; Government</span></div>
        <div class="tag-row"><span class="tag">Real Estate</span><span class="tag">Restaurants</span><span class="tag">Shoppping</span></div>
      </div>
    </section>

    <svg class="binding" width="34" height="380" viewBox="0 0 34 380">
      <g fill="none" stroke="#ffffff" stroke-width="3.5" stroke-linecap="round">
        <line x1="3" y1="4" x2="28" y2="4"/><line x1="3" y1="44" x2="28" y2="44"/>
        <line x1="3" y1="84" x2="28" y2="84"/><line x1="3" y1="124" x2="28" y2="124"/>
        <line x1="3" y1="164" x2="28" y2="164"/><line x1="3" y1="204" x2="28" y2="204"/>
        <line x1="3" y1="244" x2="28" y2="244"/><line x1="3" y1="284" x2="28" y2="284"/>
        <line x1="3" y1="324" x2="28" y2="324"/><line x1="3" y1="364" x2="28" y2="364"/>
      </g>
      <g fill="#ffffff">
        <circle cx="29" cy="4" r="3.5"/><circle cx="29" cy="44" r="3.5"/>
        <circle cx="29" cy="84" r="3.5"/><circle cx="29" cy="124" r="3.5"/>
        <circle cx="29" cy="164" r="3.5"/><circle cx="29" cy="204" r="3.5"/>
        <circle cx="29" cy="244" r="3.5"/><circle cx="29" cy="284" r="3.5"/>
        <circle cx="29" cy="324" r="3.5"/><circle cx="29" cy="364" r="3.5"/>
      </g>
    </svg>
  </main>

  <footer class="site-footer">
    <nav class="footer-links">
      <span>About Us</span><span>|</span><span>Blog</span><span>|</span><span>Business</span><span>|</span><span>Jobs</span><span>|</span><span>Privacy</span><span>|</span><span>FAQ</span><span>|</span><span>Contacts Us</span>
    </nav>
    <div class="social-links">
      <span class="dot" aria-label="Friendloop"></span>
      <span class="dot" aria-label="Chirpline"></span>
      <span class="dot" aria-label="Linkwell"></span>
      <span class="dot" aria-label="Plusora"></span>
      <svg width="16" height="12" viewBox="0 0 16 12" aria-label="Email"><rect x="0.5" y="0.5" width="15" height="11" fill="#ffffff"/><polyline points="0.5,0.5 8,7 15.5,0.5" fill="none" stroke="#ab8a1c" stroke-width="1.2"/></svg>
    </div>
  </footer>
  <div class="color-stripe bottom"></div>
</body>
</html>
```